Ethical Dilemma - Case study poster

- Create a poster/infographic detailing a real-world case study where you, as a paramedic, have encountered a patient situation that poses an ethical dilemma.
- Discuss the following principles and how they relate to the case study: beneficence, autonomy, non-maleficence and justice.
- A0 size, either landscape or portrait. Please include one or two areas for images and/or tables and graphs with backup research.
- The font must be legible, at least 12 points and 1.5 spacing with a section for all five student names to be read on the poster.
Academic project
Paramedicine and ethics

```html
<!DOCTYPE html>
<html lang="en">
<head>
<meta charset="utf-8">
<title>Ethical Dilemma – Case Study Poster</title>
<link href="https://fonts.googleapis.com/css2?family=Montserrat:wght@800;900&family=Lato:wght@400;700;900&display=swap" rel="stylesheet">
<style>
  :root{
    --bg:#3b3b3b;
    --red:#e14f2e;
    --orange:#f7831f;
    --purple:#9a2a78;
    --mauve:#c892c1;
    --grey:#ececec;
    --footer:#e4e4e4;
    --ink:#1e1e1e;
    --white:#ffffff;
    --photo-a:#d9b9a3;
    --photo-b:#efe6dc;
    --photo-c:#b7c9b8;
  }
  *{margin:0;padding:0;box-sizing:border-box}
  html,body{width:1200px;height:1200px;overflow:hidden;background:var(--bg)}
  .poster{position:absolute;left:228px;top:74px;width:744px;height:1052px;background:var(--white);overflow:hidden;font-family:"Lato",Arial,sans-serif;color:var(--ink)}
  .shapes{position:absolute;inset:0}
  .abs{position:absolute}
  .display{font-family:"Montserrat",Arial,sans-serif;font-weight:900;color:var(--white);text-transform:uppercase;line-height:1}
  .header-title{left:40px;top:10px;font-size:29px;line-height:29px}
  .header-sub{left:300px;top:14px;font-size:20px;line-height:22px;font-weight:800}
  .case-photo{left:0;top:76px;width:285px;height:171px;background:linear-gradient(120deg,var(--photo-a) 0%,var(--photo-b) 55%,var(--photo-c) 100%)}
  .case-story{left:328px;top:88px;width:404px;font-size:8.6px;line-height:12.3px;text-align:justify}
  .case-story p+p{margin-top:12px}
  .band-title{left:0;top:247px;width:744px;height:44px;display:flex;align-items:center;justify-content:center;font-size:21px;font-weight:800}
  .body-text{font-size:8.6px;line-height:12.2px}
  .space-note{font-size:9.5px;line-height:11.5px;text-transform:uppercase}
  .autonomy-text{left:24px;top:316px;width:254px;text-align:justify}
  .autonomy-note{left:24px;top:408px}
  .beneficence-text{left:420px;top:316px;width:310px;text-align:right;color:var(--white)}
  .beneficence-note{left:600px;top:361px;width:130px;text-align:right;color:var(--white)}
  .nonmal-text{left:24px;top:708px;width:256px;text-align:justify;color:var(--white)}
  .nonmal-note{left:24px;top:778px;color:var(--white)}
  .justice-text{left:492px;top:692px;width:238px;text-align:justify;color:var(--white)}
  .justice-note{left:600px;top:750px;width:130px;text-align:right;color:var(--white)}
  .label-vertical{font-size:25px;color:var(--red);transform-origin:left top;white-space:nowrap}
  .label-autonomy{left:320px;top:488px;transform:rotate(-84deg)}
  .label-justice{left:440px;top:925px;transform:rotate(-80deg);color:var(--white)}
  .label-beneficence{left:523px;top:580px;font-size:26px}
  .label-nonmal{left:24px;top:632px;font-size:26px;line-height:29px}
  .conclusion-label{left:14px;top:958px;font-size:17px;font-weight:800}
  .conclusion-text{left:190px;top:942px;width:542px;font-size:8.6px;line-height:12.3px;text-align:justify}
  .prepared-label{left:18px;top:1020px;font-family:"Montserrat",Arial,sans-serif;font-weight:900;font-size:14px;color:var(--ink)}
  .prepared-names{left:190px;top:1022px;font-size:9.5px}
</style>
</head>
<body>
<main class="poster">
  <svg class="shapes" width="744" height="1052" viewBox="0 0 744 1052" aria-hidden="true">
    <rect x="0" y="0" width="744" height="76" fill="var(--orange)"/>
    <polygon points="0,0 255,0 246,76 0,76" fill="var(--red)"/>
    <rect x="0" y="247" width="744" height="44" fill="var(--mauve)"/>
    <polygon points="0,291 334,291 371,616 0,616" fill="var(--grey)"/>
    <polygon points="334,291 744,291 744,616 371,616" fill="var(--purple)"/>
    <polygon points="0,616 371,616 438,934 0,934" fill="var(--orange)"/>
    <polygon points="371,616 744,616 744,934 438,934" fill="var(--red)"/>
    <polygon points="0,934 165,934 153,1005 0,1005" fill="var(--mauve)"/>
    <rect x="0" y="1005" width="744" height="47" fill="var(--footer)"/>
    <!-- principles hub -->
    <g class="hub">
      <circle cx="371" cy="616" r="96" fill="#ffffff" fill-opacity="0.4" stroke="#ffffff" stroke-width="2"/>
      <circle cx="371" cy="616" r="74" fill="#ffffff"/>
      <path d="M371 616 L371 542 A74 74 0 0 1 445 616 Z" fill="#ecd3e6"/>
      <path d="M371 616 L297 616 A74 74 0 0 0 371 690 Z" fill="#fde2cb"/>
      <path d="M371 616 L445 616 A74 74 0 0 1 371 690 Z" fill="#fbe0d8"/>
      <!-- gear icon -->
      <g transform="translate(336,580)" fill="var(--purple)">
        <circle r="15"/>
        <g fill="var(--purple)">
          <rect x="-3" y="-20" width="6" height="8"/><rect x="-3" y="12" width="6" height="8"/>
          <rect x="-20" y="-3" width="8" height="6"/><rect x="12" y="-3" width="8" height="6"/>
        </g>
        <circle r="6" fill="#ffffff"/>
      </g>
      <!-- two people icon -->
      <g transform="translate(406,580)" fill="var(--purple)">
        <circle cx="-8" cy="-12" r="6"/><circle cx="8" cy="-12" r="6"/>
        <path d="M-18 18 V0 a10 10 0 0 1 20 0 V18 Z"/>
        <path d="M-2 18 V0 a10 10 0 0 1 20 0 V18 Z"/>
      </g>
      <!-- heart in hand -->
      <g transform="translate(336,652)" fill="var(--orange)">
        <path d="M0 -6 C-4 -14 -16 -12 -14 -2 C-12 5 -4 9 0 13 C4 9 12 5 14 -2 C16 -12 4 -14 0 -6 Z"/>
        <path d="M-22 18 H-8 L6 24 H18 C22 24 22 19 18 19 H6" fill="none" stroke="var(--orange)" stroke-width="3.5" stroke-linecap="round" stroke-linejoin="round"/>
      </g>
      <!-- scales -->
      <g transform="translate(406,652)" stroke="var(--red)" stroke-width="3" fill="none" stroke-linecap="round">
        <line x1="0" y1="-18" x2="0" y2="18"/><line x1="-18" y1="-12" x2="18" y2="-12"/>
        <line x1="-10" y1="20" x2="10" y2="20"/>
        <path d="M-18 -12 L-25 4 H-11 Z"/><path d="M18 -12 L11 4 H25 Z"/>
      </g>
    </g>
  </svg>

  <h1 class="abs display header-title">Ethical<br>Dilemma</h1>
  <h2 class="abs display header-sub">Challenging Family Dynamics<br>in an Emergency Setting</h2>

  <div class="abs case-photo" role="img" aria-label="Photo of a distressed young woman embracing a crying child at home"></div>
  <div class="abs case-story">
    <p>Responding to a distress call from a patient stating a drug overdose. Upon arriving, the patient's mother greets you at the door, concerned and anxious. The patient emerges from the house, looking distressed and is guided to the ambulance for initial observations. During the conversation, she admits to feeling suicidal and reveals that, at times, her parents have locked her in the garden shed. Concerned for her well-being, you impress the need to present to the hospital.</p>
    <p>The patient agrees to seek further help and returns to the hospital to collect some personal belongings. As she reappears, her mother by her side, there is a noticeable change in the atmosphere. Her mother appears tense and denies any issues. The patient's demeanour has also shifted, echoing her mother and denying thoughts of suicide and the apparent overdose. Her mother has now called the police. It is very clear that the family has tension and disagreement regarding their daughter's condition and the appropriate course of action for her medical needs.</p>
  </div>

  <h2 class="abs display band-title">Application of Bioethical Principles</h2>

  <p class="abs body-text autonomy-text">While the patient initially expressed her desire for medical help, her subsequent change of heart raises concerns. Her independence should be respected, but a careful assessment of her decision-making capacity is crucial, given the potential for external influence or mental health issues.</p>
  <p class="abs space-note autonomy-note">Space for<br>additional text<br>graph, table</p>
  <h3 class="abs display label-vertical label-autonomy">Autonomy</h3>

  <p class="abs body-text beneficence-text">Given her history of suicidal thoughts and the conflicting messages, your primary responsibility is her well-being. Acting in her best interest is paramount if you suspect she's being coerced or manipulated</p>
  <p class="abs space-note beneficence-note">Space for<br>additional text<br>graph, table</p>
  <h3 class="abs display label-beneficence">Beneficence</h3>

  <h3 class="abs display label-nonmal">Non<br>Maleficence</h3>
  <p class="abs body-text nonmal-text">Your role is to ensure that her actions are not compromised by undue pressure or emotional manipulation from her mother. If you sense harm could come to her due to the situation, steps must be taken to protect her.</p>
  <p class="abs space-note nonmal-note">Space for<br>additional text<br>graph, table</p>

  <p class="abs body-text justice-text">While considering the patient's mother's perspective, your ultimate priority remains the patient's welfare and safety. Balance her mother's role with your duty to safeguard the patient from harm.</p>
  <p class="abs space-note justice-note">Space for<br>additional text<br>graph, table</p>
  <h3 class="abs display label-vertical label-justice">Justice</h3>

  <h2 class="abs display conclusion-label">Conclusion</h2>
  <p class="abs conclusion-text">The situation is complex, involving potential coercion, mental health concerns, and disagreement within the family. Collaboration with medical professionals and possibly involving the police might be necessary to ensure her safety and well-being. Although you should strive to honour the patient's autonomy, you have a duty to intervene if her current stance is influenced by factors that put her at risk. Ultimately, your actions should align with the principles of protecting her from harm and prioritising her overall welfare.</p>

  <p class="abs prepared-label">Prepared by:</p>
  <p class="abs prepared-names">Name 1, Name 2, Name 3, Name 4, Name 5</p>
</main>
</body>
</html>
```